Flight school sign for building, banner, and bilboard

This sign is primarily for use on the side of our flight school building to draw attention for current and future flight school students. We offer airplane and helicopter flight training, ground school training and seminars, airplane and helicopter rentals, multi-engine training, and more. I would like a professional but exciting sign that can be used across a multitude of signage options such as banners, banner ads, billboard, and other mediums so that our sign is consistent and recognizable.

Contact Information for Business Card

The business card should match our company sign somewhat but not exactly. We want good and exciting imagery or wording and energizing/exciting colors.

```html
<!DOCTYPE html>
<html lang="en">
<head>
<meta charset="utf-8">
<title>Skyward Aviation – Flight School Banner</title>
<link rel="stylesheet" href="https://fonts.googleapis.com/css2?family=Barlow+Condensed:wght@500;600;700&family=Barlow:wght@500&family=Oswald:wght@500&display=swap">
<style>
  :root {
    --navy: #222a5e;
    --red: #e8283a;
    --white: #ffffff;
    --sky-light: #e6eef4;
    --sky-mid: #a9b8c6;
    --stage: #3a3a3a;
  }
  html, body {
    margin: 0;
    padding: 0;
    width: 1000px;
    height: 1200px;
    overflow: hidden;
    background: var(--stage);
  }
  .banner {
    position: absolute;
    left: 30px;
    top: 435px;
    width: 940px;
    height: 330px;
    background: var(--navy);
    overflow: hidden;
    box-shadow: 0 12px 30px rgba(0,0,0,.45);
  }
  .banner-art {
    position: absolute;
    inset: 0;
    width: 940px;
    height: 330px;
  }
  .brand {
    position: absolute;
    left: 30px;
    top: 96px;
    width: 270px;
    text-align: center;
    color: var(--white);
  }
  .brand-name {
    font-family: "Barlow", sans-serif;
    font-weight: 500;
    font-size: 25px;
    letter-spacing: 1px;
    line-height: 1;
  }
  .brand-tagline {
    margin-top: 5px;
    font-family: "Barlow", sans-serif;
    font-weight: 500;
    font-size: 8px;
    letter-spacing: 7px;
  }
  .services {
    position: absolute;
    top: 160px;
    margin: 0;
    padding: 0;
    list-style: none;
    font-family: "Oswald", sans-serif;
    font-weight: 500;
    font-size: 17px;
    line-height: 24px;
    color: var(--white);
    text-transform: uppercase;
  }
  .services li {
    position: relative;
    padding-left: 20px;
    margin-bottom: 8px;
  }
  .services li::before {
    content: "»";
    position: absolute;
    left: 0;
    top: -3px;
    color: var(--red);
    font-size: 24px;
  }
  .services-left { left: 37px; }
  .services-right { left: 270px; }
  .headline {
    position: absolute;
    left: 456px;
    top: 22px;
    font-family: "Barlow Condensed", sans-serif;
    font-weight: 700;
    line-height: .95;
    margin: 0;
  }
  .headline-top {
    display: block;
    color: var(--navy);
    font-size: 40px;
  }
  .headline-main {
    display: block;
    color: var(--red);
    font-size: 60px;
  }
  .contact {
    position: absolute;
    top: 281px;
    display: flex;
    align-items: center;
    gap: 8px;
    font-family: "Barlow Condensed", sans-serif;
    font-weight: 600;
    font-size: 29px;
    line-height: 40px;
  }
  .contact-web { left: 36px; color: var(--red); }
  .contact-phone { left: 370px; color: var(--white); }
  .contact svg { width: 22px; height: 22px; }
</style>
</head>
<body>
<main class="banner">
  <svg class="banner-art" viewBox="0 0 940 330" aria-hidden="false">
    <defs>
      <linearGradient id="photo-tones" x1="0" y1="0" x2="1" y2="1">
        <stop offset="0" stop-color="var(--sky-light)"/>
        <stop offset=".55" stop-color="var(--sky-mid)"/>
        <stop offset="1" stop-color="#4a5878"/>
      </linearGradient>
    </defs>
    <path class="photo-area" role="img" aria-label="Photo of a smiling student pilot with headset in an open-canopy training aircraft cockpit"
          fill="url(#photo-tones)"
          d="M300 0 L800 0 C880 40 930 150 915 240 C905 290 840 292 760 285 C620 270 470 200 390 110 Z"/>
    <path class="swoosh-white" fill="var(--white)"
          d="M388 104 C470 210 640 300 800 312 L800 318 C630 305 460 220 384 110 Z"/>
    <path class="swoosh-red" fill="var(--red)"
          d="M392 108 C480 215 650 300 790 305 C860 307 905 285 915 240 C925 190 910 120 850 40 C910 90 940 150 940 200 L940 330 L800 330 C640 310 470 220 392 108 Z"/>
    <path class="swoosh-navy-edge" fill="none" stroke="var(--navy)" stroke-width="3"
          d="M915 240 C905 290 840 292 760 285"/>
    <path class="band-web" fill="var(--white)" d="M0 273 L357 273 L327 330 L0 330 Z"/>
    <path class="band-phone" fill="var(--red)" d="M357 273 L700 273 C740 300 770 318 800 330 L327 330 Z"/>
    <path class="plane-graphic" role="img" aria-label="Red airplane graphic" fill="var(--red)"
          d="M300 0 L330 0 L412 95 L395 102 Z"/>
  </svg>

  <div class="brand">
    <div class="brand-name">SKYWARD AVIATION</div>
    <div class="brand-tagline">LEARN TO FLY</div>
  </div>

  <ul class="services services-left">
    <li>Airplane and<br>helicopter flight training</li>
    <li>Airplane and<br>helicopter rentals</li>
  </ul>
  <ul class="services services-right">
    <li>Ground school<br>training and seminars</li>
    <li>Multi-engine training,<br>and more.</li>
  </ul>

  <h1 class="headline">
    <span class="headline-top">EXCELLENCE IN</span>
    <span class="headline-main">AVIATION</span>
  </h1>

  <div class="contact contact-web">
    <svg viewBox="0 0 24 24" fill="none" stroke="var(--navy)" stroke-width="1.8">
      <circle cx="12" cy="12" r="10"/>
      <ellipse cx="12" cy="12" rx="4.5" ry="10"/>
      <path d="M2 12 H22 M4 7 H20 M4 17 H20"/>
    </svg>
    <span>SkywardAviation.com</span>
  </div>
  <div class="contact contact-phone">
    <svg viewBox="0 0 24 24" fill="none" stroke="var(--white)" stroke-width="1.8">
      <circle cx="12" cy="12" r="10.5"/>
      <path d="M8.5 6.5 L10.5 9 L9.3 10.6 C10 12.3 11.5 13.9 13.3 14.7 L14.9 13.5 L17.4 15.5 L16.2 17.3 C11.5 17 7 12.5 6.7 7.8 Z"/>
    </svg>
    <span>(555) 214 0187</span>
  </div>
</main>
</body>
</html>
```